Building Servicess

We need a new business card design for a company. We specialise in: Electrical/Site temporary electrics, Data/Network Installation, Passive Fire Protection

Industry/Entity Type

Construction

Contact Information for Business Card

Services provided as detailed on project description

Font styles to use
Serif

Colors
0054AA
0677BA
7BADD7
CADEEF
E8F1F8
00AB8E
00BBA5
67D7C9
C6EFE9
E9F9F6
EB3D1F
EC4F4E
F09395
F8D3D4
FCEDEE

Requirements
Must have
• Company logo-contact details-phone numbers

```html
<!DOCTYPE html>
<html lang="en">
<head>
<meta charset="utf-8">
<title>Orbis Site Services – Business Card</title>
<link rel="stylesheet" href="https://fonts.googleapis.com/css2?family=Open+Sans:wght@400;600;700&display=swap">
<style>
  :root {
    --backdrop: #383838;
    --card: #161616;
    --card-back: #121212;
    --pattern-tone: #1c1c1c;
    --brand-blue: #1a7bd0;
    --brand-grey: #8a8a8a;
    --text-light: #e6e6e6;
    --text-muted: #7c7c7c;
  }
  * { box-sizing: border-box; margin: 0; padding: 0; }
  html, body {
    width: 1200px; height: 801px; overflow: hidden;
    background: var(--backdrop);
    font-family: "Open Sans", Arial, sans-serif;
  }
  .canvas {
    width: 1200px; height: 801px;
    display: flex; align-items: center; justify-content: center; gap: 40px;
  }
  .card {
    position: relative;
    width: 540px; height: 310px;
    border-bottom: 3px solid var(--brand-blue);
    overflow: hidden;
  }
  .card--front { background: var(--card); }
  .card--back { background: var(--card-back); }

  /* front */
  .brand {
    position: absolute; left: 40px; top: 0; bottom: 0; width: 230px;
    display: flex; flex-direction: column; justify-content: center; align-items: flex-start;
  }
  .brand__name {
    display: flex; align-items: center; gap: 10px;
    color: var(--brand-blue); font-weight: 700; font-size: 24px; letter-spacing: 1px;
    text-transform: uppercase; line-height: 1.1;
  }
  .brand__dot { width: 14px; height: 14px; background: var(--brand-blue); flex: none; }
  .brand__rule { width: 200px; height: 1px; background: var(--brand-grey); margin-top: 10px; }
  .brand__suffix {
    color: var(--brand-grey); font-size: 10px; letter-spacing: 6px; margin-top: 6px; align-self: flex-end;
    margin-right: 30px;
  }
  .divider {
    position: absolute; left: 290px; top: 70px; bottom: 70px; width: 1px; background: var(--brand-blue);
  }
  .details {
    position: absolute; left: 310px; top: 62px; right: 20px;
    color: var(--text-light); font-size: 12px; line-height: 1.45;
  }
  .details__name { color: var(--brand-blue); font-weight: 700; font-size: 17px; text-transform: uppercase; letter-spacing: .5px; }
  .details__role { color: var(--text-muted); font-size: 12px; margin-bottom: 8px; }
  .details__address { margin-bottom: 8px; }
  .contact { list-style: none; }
  .contact li { display: flex; align-items: center; gap: 7px; }
  .contact svg { width: 11px; height: 11px; flex: none; }

  /* back */
  .back-pattern { position: absolute; inset: 0; background: linear-gradient(135deg, var(--pattern-tone), var(--card-back)); }
  .back-mark {
    position: absolute; right: 90px; top: 140px;
    display: flex; align-items: center; gap: 8px;
    color: var(--brand-blue); font-weight: 700; font-size: 22px; letter-spacing: 1px;
  }
  .back-mark .brand__dot { width: 12px; height: 12px; }
</style>
</head>
<body>
<main class="canvas">
  <section class="card card--front">
    <div class="brand">
      <div class="brand__name"><span class="brand__dot"></span>Orbis<br>Site Services</div>
      <div class="brand__rule"></div>
      <div class="brand__suffix">LTD</div>
    </div>
    <div class="divider"></div>
    <div class="details">
      <p class="details__name">Marek Dalton</p>
      <p class="details__role">Managing Director</p>
      <p class="details__address">1840 Harbor Crest Way<br>Bayview CA 90312</p>
      <ul class="contact">
        <li><svg viewBox="0 0 12 12"><path d="M3 1l2 2.5-1.2 1.2a6 6 0 003.5 3.5L8.5 7 11 9l-1.5 2C5 11 1 7 1 2.5z" fill="var(--brand-blue)"/></svg>020 4187 3391</li>
        <li><svg viewBox="0 0 12 12"><rect x="3" y="1" width="6" height="10" rx="1" fill="none" stroke="var(--text-light)" stroke-width="1.2"/></svg>075 2219 6604</li>
        <li><svg viewBox="0 0 12 12"><rect x="1" y="3" width="10" height="7" fill="var(--brand-blue)"/><path d="M1 3l5 4 5-4" fill="none" stroke="var(--card)" stroke-width="1"/></svg>info@orbissiteservices.com</li>
        <li><svg viewBox="0 0 12 12"><circle cx="6" cy="6" r="5" fill="var(--brand-blue)"/><path d="M1 6h10M6 1c-2 3-2 7 0 10M6 1c2 3 2 7 0 10" fill="none" stroke="var(--card)" stroke-width=".8"/></svg>www.orbissiteservices.com</li>
      </ul>
    </div>
  </section>

  <section class="card card--back">
    <div class="back-pattern" role="img" aria-label="Repeating embossed brand pattern in black tones"></div>
    <div class="back-mark"><span class="brand__dot"></span>Orbis</div>
  </section>
</main>
</body>
</html>
```